International Vacuum Business Needs a Business Card

We need a business card design for a new company based in Toronto called "Duvo-Sweep". We will be selling and installing a proprietary central vacuum system that is one of a kind to the condominium market mainly through various large builders throughout the country as well as a second distribution chain at a retail level. Our product has a very unique retractable hose system that allows the hose to be stored away within the walls of a space all by the push of a button. "No more hoses laying around the house" We would like to see the design use the colours Red, Black, Grey and possibly white. The design should communicate the following terms " sleek, discreet, convenient, sophisticated, modern"
Updates

Project Deadline Extended
Reason: Hello All, I have not been able to provide very much feedback as I have been unavailable this week so we will be extending the deadline for another 3 days. Thanks,

Project Deadline Extended
Reason: Hello All, The revision and feedback process has been slow so I have no choice but to extend once again. We are still looking for that one great design. Thank you

Project Deadline Extended
Reason: Guys the feedback and changes on some of the designs are taking really long from some of you so I have no choice but to continue extending the deadline forward.

Target Market(s)

Our target market is male/female aged 25-65, more so focussing on 25-50.

Industry/Entity Type

Retail

Requirements
Must have
• Phone #
Fax #
Mobile #
Toll Free #
Web site address "www.duvosweep.ca"

```html
<!DOCTYPE html>
<html lang="en">
<head>
<meta charset="utf-8">
<title>Duvo-Sweep Business Card</title>
<link rel="stylesheet" href="https://fonts.googleapis.com/css2?family=Exo+2:wght@200;300&family=Lato:wght@400;700&display=swap">
<style>
  :root {
    --backdrop: #e9e9e9;
    --card-black: #181818;
    --brand-red: #e0202a;
    --text-grey: #454545;
    --name-grey: #4a4a4a;
  }
  * { box-sizing: border-box; margin: 0; padding: 0; }
  html, body {
    width: 1200px;
    height: 900px;
    overflow: hidden;
    background: var(--backdrop);
  }
  .canvas {
    position: relative;
    width: 1200px;
    height: 900px;
  }
  .card {
    position: absolute;
    left: 250px;
    width: 700px;
    height: 400px;
    background: var(--card-black);
    box-shadow: 0 6px 18px rgba(0, 0, 0, 0.18);
  }
  .card--back { top: 40px; }
  .card--front { top: 460px; }

  /* Back face: brand name stands large and centred */
  .card--back .brand-mark {
    position: absolute;
    inset: 0;
    display: flex;
    align-items: center;
    justify-content: center;
    gap: 22px;
  }
  .brand-square {
    display: block;
    background: var(--brand-red);
  }
  .card--back .brand-square { width: 64px; height: 64px; }
  .card--back .brand-name {
    font-family: "Exo 2", sans-serif;
    font-weight: 300;
    font-size: 52px;
    color: var(--brand-red);
    letter-spacing: 1px;
  }

  /* Front face */
  .brand-lockup {
    position: absolute;
    left: 62px;
    top: 170px;
    display: flex;
    align-items: center;
    gap: 10px;
  }
  .card--front .brand-square { width: 38px; height: 38px; }
  .lockup-rule {
    width: 2px;
    height: 40px;
    background: var(--brand-red);
  }
  .card--front .brand-name {
    font-family: "Exo 2", sans-serif;
    font-weight: 200;
    font-size: 40px;
    color: var(--name-grey);
    letter-spacing: 1px;
  }
  .section-divider {
    position: absolute;
    left: 440px;
    top: 110px;
    width: 2px;
    height: 150px;
    background: var(--brand-red);
  }
  .contact-list {
    position: absolute;
    left: 470px;
    top: 118px;
    list-style: none;
    font-family: "Lato", sans-serif;
    font-size: 15px;
    line-height: 26px;
  }
  .contact-label {
    font-weight: 700;
    color: var(--brand-red);
  }
  .contact-value {
    font-weight: 400;
    color: var(--text-grey);
    letter-spacing: 0.5px;
  }
</style>
</head>
<body>
<main class="canvas">
  <section class="card card--back" aria-label="Card back">
    <div class="brand-mark">
      <span class="brand-square" aria-hidden="true"></span>
      <span class="brand-name">Duvo-Sweep</span>
    </div>
  </section>

  <section class="card card--front" aria-label="Card front">
    <div class="brand-lockup">
      <span class="brand-square" aria-hidden="true"></span>
      <span class="lockup-rule" aria-hidden="true"></span>
      <span class="brand-name">Duvo-Sweep</span>
    </div>
    <span class="section-divider" aria-hidden="true"></span>
    <ul class="contact-list">
      <li><span class="contact-label">Phone:</span> <span class="contact-value">555-555-555</span></li>
      <li><span class="contact-label">Fax:</span> <span class="contact-value">555-555-555</span></li>
      <li><span class="contact-label">Mobile:</span> <span class="contact-value">000-00000000</span></li>
      <li><span class="contact-label">Toll Free:</span> <span class="contact-value">000-00000000</span></li>
      <li><span class="contact-label">Web:</span> <span class="contact-value">www.duvosweep.ca</span></li>
    </ul>
  </section>
</main>
</body>
</html>
```